Brightwater Facility Partners Business card

We wish to have a professional Business card to present to large Corporate CEO's ASAP.

Our web site helps explain our business www.brightwaterfp.org

Brightwater Facility Partners was established after we discovered how difficult it is to organise outsourced services while heading up a business or company.

We act as a facilitator for businesses who don't have the desire, expertise or recourses to manage their own systems and meet all their requirements.

We provide an all in one facility management solution for all types of businesses. We manage schedules, contractors and costs on behalf of businesses and their needs and wants.

Having an extensive network ensures we are able to connect businesses with the right service providers.

Target Market(s)

Company CEO

Industry/Entity Type

Business

Font styles to use
Sans Serif

Colors
33a6d7
f9fdfe
0355a3

Requirements
Must have
• professional design
Nice to have
• colours to match logo

```html
<!DOCTYPE html>
<html lang="en">
<head>
<meta charset="utf-8">
<title>Brightwater Facility Partners – Business Card</title>
<link href="https://fonts.googleapis.com/css2?family=Questrial&display=swap" rel="stylesheet">
<style>
  :root {
    --sky: #33a6d7;
    --navy: #0355a3;
    --paper: #f9fdfe;
    --stage: #d3d3d3;
    --ink: #1d1d1f;
    --caption: #4a4246;
    --rule: #c9d3da;
  }
  * { margin: 0; padding: 0; box-sizing: border-box; }
  html, body {
    width: 1200px; height: 985px; overflow: hidden;
    background: var(--stage);
    font-family: "Questrial", "Century Gothic", sans-serif;
  }
  .stage { position: relative; width: 1200px; height: 985px; }

  .card {
    position: absolute; top: 330px;
    width: 510px; height: 290px;
    background: var(--paper);
    overflow: hidden;
  }
  .card--front { left: 70px; }
  .card--back { left: 620px; }

  .card__band {
    position: absolute; left: 0; bottom: 0;
    width: 100%; height: 15px;
  }

  .brand {
    position: absolute;
    display: flex; align-items: center; gap: 9px;
  }
  .brand__dot {
    width: 22px; height: 22px; border-radius: 50%;
    background: var(--navy); flex: none;
  }
  .brand__name {
    color: var(--navy);
    font-size: 14px; letter-spacing: 0.5px; line-height: 1.3;
    text-transform: uppercase;
  }
  .card--front .brand { left: 38px; top: 118px; }
  .card--front .brand__name { width: 185px; }

  .card--back .brand { left: 0; right: 0; top: 116px; justify-content: center; gap: 7px; }
  .card--back .brand__name { font-size: 11px; width: 145px; }
  .card--back .brand__dot { width: 18px; height: 18px; }

  .divider { position: absolute; left: 0; top: 0; }

  .contact { position: absolute; left: 309px; top: 112px; }
  .contact__name { color: var(--sky); font-size: 13px; margin-bottom: 11px; }
  .contact__row { display: flex; color: var(--ink); font-size: 9px; line-height: 14px; }
  .contact__label { width: 53px; }

  .web {
    position: absolute; left: 0; right: 0; bottom: 23px;
    text-align: center; color: var(--ink); font-size: 9px;
  }

  .caption {
    position: absolute; top: 650px; width: 510px;
    text-align: center; color: var(--caption); font-size: 19px;
  }
  .caption--front { left: 70px; }
  .caption--back { left: 620px; }
</style>
</head>
<body>
<main class="stage">

  <section class="card card--front" aria-label="Business card front">
    <div class="brand">
      <span class="brand__dot"></span>
      <span class="brand__name">Brightwater Facility Partners</span>
    </div>
    <svg class="divider" width="510" height="290" aria-hidden="true">
      <line x1="306" y1="73" x2="254" y2="193" stroke="var(--rule)" stroke-width="1"/>
    </svg>
    <div class="contact">
      <p class="contact__name">Daniel Hartley</p>
      <p class="contact__row"><span class="contact__label">Contact</span><span>: 0400 218 736</span></p>
      <p class="contact__row"><span class="contact__label">Email</span><span>: daniel@brightwaterfp.org</span></p>
    </div>
    <svg class="card__band" viewBox="0 0 510 15" preserveAspectRatio="none" aria-hidden="true">
      <rect width="510" height="15" fill="var(--sky)"/>
      <polygon points="226,15 232,0 510,0 510,15" fill="var(--navy)"/>
    </svg>
  </section>

  <section class="card card--back" aria-label="Business card back">
    <div class="brand">
      <span class="brand__dot"></span>
      <span class="brand__name">Brightwater Facility Partners</span>
    </div>
    <p class="web">www.brightwaterfp.org</p>
    <svg class="card__band" viewBox="0 0 510 15" preserveAspectRatio="none" aria-hidden="true">
      <rect width="510" height="15" fill="var(--sky)"/>
    </svg>
  </section>

  <p class="caption caption--front">Front</p>
  <p class="caption caption--back">Back</p>

</main>
</body>
</html>
```